Simplified minimalist but bold website

Design a website for a brand 'Brighten Every Morning' that shares ideas to make managing home and health easier through email swap series, webinars and eventually courses.

Simple landing page to attract users to sign up for a freebie.

Target Market(s)

women with families & homes to run

Number of Pages Required

1 page

Font styles to use
Sans Serif

Colors
e667a6
b768aa
acd136
ffffff
959595

Requirements
Must have
• Simplified look, line icons, opt-in template, contact us form

```html
<!DOCTYPE html>
<html lang="en">
<head>
<meta charset="utf-8">
<title>Brighten Every Morning – Landing Page Screens</title>
<link href="https://fonts.googleapis.com/css2?family=Josefin+Sans:wght@300;400;600&family=Josefin+Slab:wght@300;400&display=swap" rel="stylesheet">
<style>
  :root{
    --pink:#e667a6;
    --pink-soft:#fbe3ef;
    --plum:#b768aa;
    --plum-soft:#f3e5f1;
    --lime:#acd136;
    --lime-soft:#f5f8e6;
    --sky:#35a6d6;
    --sky-soft:#e3f2f8;
    --grey:#959595;
    --ink:#444;
    --white:#ffffff;
    --backdrop:#fbeef5;
  }
  *{box-sizing:border-box;margin:0;padding:0}
  html,body{width:1200px;height:1200px;overflow:hidden;background:var(--backdrop)}
  body{position:relative;font-family:"Josefin Sans",sans-serif;color:var(--ink)}

  .screen{position:absolute;background:var(--white);overflow:visible;
    transform:translate(-50%,-50%) rotate(-15deg)}
  .screen--hero{left:290px;top:300px;width:620px;height:310px}
  .screen--swaps{left:868px;top:200px;width:580px;height:290px}
  .screen--declutter{left:320px;top:700px;width:620px;height:310px}
  .screen--series{left:895px;top:555px;width:600px;height:320px}
  .screen--contact{left:752px;top:1000px;width:600px;height:380px}

  .frame{position:absolute;border:4px solid;pointer-events:none}

  .social{position:absolute;left:20px;bottom:-50px;width:40px;padding:14px 0 10px;
    display:flex;flex-direction:column;gap:12px;align-items:center;
    font-size:7px;line-height:1;color:var(--white);text-transform:uppercase;letter-spacing:.5px;z-index:2}
  .social span{display:block;text-align:center}
  .screen--declutter .social{bottom:-70px}

  .pager{position:absolute;right:-10px;bottom:20px;width:95px;height:40px;
    display:flex;justify-content:center;align-items:center;gap:26px;font-size:12px}

  .rule{width:38px;height:1px;margin:8px auto}
  .eyebrow{font-family:"Josefin Slab",serif;font-size:10px}
  .heading{font-size:16px;font-weight:400;color:var(--ink);margin:4px 0 6px}
  .small{font-size:6.5px;line-height:1.6;color:var(--grey)}
  .link{font-size:7px;font-weight:600;border-bottom:1px dotted;display:inline-block;margin-right:16px}

  .optin{position:absolute;top:0;right:40px;width:220px;height:200px;padding:40px 20px}
  .optin label{display:block;font-family:"Josefin Slab",serif;font-size:7px;margin-top:10px}
  .optin .field{height:18px;border:1px solid;background:var(--white);margin-top:2px}
  .btn{display:block;text-align:center;color:var(--white);font-size:8px;padding:7px 0;margin-top:14px}

  .hero-copy{position:absolute;left:0;right:0;top:100px;text-align:center}
  .hero-copy h1{font-family:"Josefin Slab",serif;font-weight:300;font-size:34px;color:var(--pink)}
  .hero-copy p{font-size:10px;color:var(--grey);line-height:1.7}

  .intro{position:absolute;left:40px;top:60px;width:230px;z-index:1}
  .screen--declutter .intro{top:120px}

  .series-copy{position:absolute;left:0;right:0;top:70px;text-align:center}
  .series-copy h2{font-family:"Josefin Slab",serif;font-weight:300;font-size:22px;color:var(--sky)}
  .series-copy p{font-size:8.5px;color:var(--grey);line-height:1.6;margin-bottom:8px}
  .series-copy .btn{width:150px;margin:6px auto 0}

  .contact-form{position:absolute;left:150px;top:70px;width:250px;text-align:left}
  .contact-form h2{font-family:"Josefin Slab",serif;font-weight:300;font-size:22px;color:var(--pink);text-align:center}
  .contact-form label{display:block;font-family:"Josefin Slab",serif;font-size:7px;color:var(--pink);margin-top:8px}
  .contact-form .field{height:20px;border:1px solid var(--pink);margin-top:2px}
  .contact-form .field--message{height:80px}
  .contact-form .btn{width:150px;margin:14px auto 0}
</style>
</head>
<body>

<section class="screen screen--hero">
  <div class="frame" style="left:-10px;top:-4px;width:160px;height:200px;border-color:var(--pink-soft)"></div>
  <div class="frame" style="right:-4px;bottom:-4px;width:210px;height:160px;border-color:var(--lime-soft)"></div>
  <div class="hero-copy">
    <h1>Brighten Every Morning.</h1>
    <div class="rule" style="background:var(--pink)"></div>
    <p>Chances are life is a little overwhelming.<br>Let us Help</p>
  </div>
  <nav class="social" style="background:var(--pink)"><span>Circ<br>le</span><span>Chir<br>per</span><span>Snap<br>shot</span><span>Pin<br>board</span></nav>
  <div class="pager" style="background:var(--pink-soft);color:var(--pink)"><span>&lsaquo;</span><span>&rsaquo;</span></div>
</section>

<section class="screen screen--swaps">
  <div class="frame" style="left:-4px;top:-4px;width:200px;height:90px;border-color:var(--plum-soft)"></div>
  <div class="intro">
    <p class="eyebrow" style="color:var(--plum)">Baby Steps... (try out a few of our tricks)</p>
    <h2 class="heading">Swaps Email Series</h2>
    <div class="rule" style="background:var(--plum);margin-left:0"></div>
    <p class="small">Save TIME, MONEY and SANITY with simple product swaps.</p>
    <p class="small">Reduce the amount of work it takes to run your home.<br>Swap out existing products for more convenient ones.<br>Each swap saves you work, clutter, time &amp; money.</p>
    <p style="margin-top:8px"><span class="link" style="color:var(--plum)">See Sample Swaps</span><span class="link" style="color:var(--plum)">Learn More</span></p>
  </div>
  <form class="optin" style="background:var(--plum-soft)">
    <label style="color:var(--plum)">Name</label><div class="field" style="border-color:var(--plum)"></div>
    <label style="color:var(--plum)">Email</label><div class="field" style="border-color:var(--plum)"></div>
    <span class="btn" style="background:var(--plum)">Sign Me Up!</span>
  </form>
  <nav class="social" style="background:var(--plum)"><span>Circ<br>le</span><span>Chir<br>per</span><span>Snap<br>shot</span><span>Pin<br>board</span></nav>
  <div class="pager" style="background:var(--plum-soft);color:var(--plum)"><span>&lsaquo;</span><span>&rsaquo;</span></div>
</section>

<section class="screen screen--declutter">
  <div class="frame" style="left:-4px;top:20px;width:200px;height:130px;border-color:var(--lime-soft)"></div>
  <div class="intro">
    <p class="eyebrow" style="color:var(--lime)">Big Leap... (I'm ready to roll up my sleeves)</p>
    <h2 class="heading">Decluttering Guide</h2>
    <div class="rule" style="background:var(--lime);margin-left:0"></div>
    <p class="small">Declutter your home...</p>
    <p style="margin-top:6px"><span class="link" style="color:var(--lime)">Learn More</span></p>
  </div>
  <form class="optin" style="background:var(--lime-soft);top:20px;right:130px;height:240px;padding-top:90px">
    <label style="color:var(--lime)">Name</label><div class="field" style="border-color:var(--lime)"></div>
    <label style="color:var(--lime)">Email</label><div class="field" style="border-color:var(--lime)"></div>
    <span class="btn" style="background:var(--lime)">Send Me The Guide!</span>
  </form>
  <nav class="social" style="background:var(--lime)"><span>Circ<br>le</span><span>Chir<br>per</span><span>Snap<br>shot</span><span>Pin<br>board</span></nav>
  <div class="pager" style="background:var(--lime-soft);color:var(--lime)"><span>&lsaquo;</span><span>&rsaquo;</span></div>
</section>

<section class="screen screen--series">
  <div class="frame" style="left:200px;top:-4px;width:190px;height:190px;border-color:var(--sky-soft)"></div>
  <div class="series-copy">
    <h2>Swaps Email Series</h2>
    <div class="rule" style="background:var(--sky)"></div>
    <p>Save TIME, MONEY and SANITY with simple product swaps.<br>And reduce the amount of work it takes to run your home.<br>Swap out existing products for more convenient ones.<br>Each swap save you work, clutter, time &amp; money.</p>
    <p>You get an email 2x weekly for 6-12 weeks only<br>Get even more if you feel they are helpful to you</p>
    <p>Join our monthly SIMPLE SWAP SHARING web jams with other mums and get even more ideas.<br>Better yet, come with great tips of your own to share</p>
    <span class="btn" style="background:var(--sky)">Sign Me Up!</span>
  </div>
  <nav class="social" style="background:var(--sky)"><span>Circ<br>le</span><span>Chir<br>per</span><span>Snap<br>shot</span><span>Pin<br>board</span></nav>
  <div class="pager" style="background:var(--sky-soft);color:var(--sky)"><span>&lsaquo;</span><span>&rsaquo;</span></div>
</section>

<section class="screen screen--contact">
  <div class="frame" style="right:-4px;top:-4px;width:200px;height:140px;border-color:var(--pink-soft)"></div>
  <form class="contact-form">
    <h2>Contact Us</h2>
    <div class="rule" style="background:var(--pink)"></div>
    <label>Name</label><div class="field"></div>
    <label>Email</label><div class="field"></div>
    <label>Message</label><div class="field field--message"></div>
    <span class="btn" style="background:var(--pink)">Sign Me Up!</span>
  </form>
  <nav class="social" style="background:var(--pink)"><span>Circ<br>le</span><span>Chir<br>per</span><span>Snap<br>shot</span><span>Pin<br>board</span></nav>
  <div class="pager" style="background:var(--pink-soft);color:var(--pink)"><span>&lsaquo;</span><span>&rsaquo;</span></div>
</section>

</body>
</html>
```